Casas de Nueva Aurora Flyer

Make me a flyer postcard 5 x 7 horizontal, one sided. I want main title to be "Casas de Nueva Aurora". It needs to say “Familias que se forman en la fe y valores humanos, y trabajan para llevar a otras familias al encuentro con Cristo y la Virgen María.”  We are in 4 places, include this:
Reuniones Cada Domingo
Monte Tabor Alto, Falls Church: 11:15am - 301-555-0142
Luz Divina Norte, Sterling: 9:30am - 571-555-0187
Hogar Manassas Park, 9:45am - 703-555-0129
Paz Eterna Sur, Winchester: 2:30pm - 540-555-0163
Include the logo attached, and use the picture attached as the main image, you can select the people from the image only and delete background or keep background but make it fit in nicely to the postcard.

```html
<!DOCTYPE html>
<html lang="es">
<head>
<meta charset="utf-8">
<title>Casas de Nueva Aurora – Postal</title>
<link href="https://fonts.googleapis.com/css2?family=Outfit:wght@700&family=Roboto:wght@500;700&display=swap" rel="stylesheet">
<style>
  :root {
    --page-bg: #e9e9e9;
    --crimson: #c8334a;
    --gold-band: #c9994e;
    --ink-dark: #3a3a3a;
    --yellow: #fff200;
    --white: #ffffff;
    --leaf-dark: #3f6b35;
    --leaf-light: #8fb27a;
    --sky: #c9d6e0;
  }
  * { margin: 0; padding: 0; box-sizing: border-box; }
  html, body {
    width: 1200px; height: 949px; overflow: hidden;
    background: var(--page-bg);
  }
  .postcard {
    position: absolute; left: 105px; top: 133px;
    width: 977px; height: 698px;
    background: var(--crimson);
    overflow: hidden;
  }
  .hero {
    position: absolute; left: 0; top: 0; width: 977px; height: 391px;
  }
  .group-photo {
    position: absolute; inset: 0;
    background:
      linear-gradient(180deg, rgba(200,51,74,0) 55%, rgba(200,51,74,0.55) 82%, rgba(200,51,74,0.9) 100%),
      radial-gradient(ellipse at 55% 70%, #b79a8a 0%, #8c7a86 35%, rgba(120,110,120,0) 70%),
      linear-gradient(180deg, var(--sky) 0%, var(--leaf-light) 18%, var(--leaf-dark) 45%, #6b6a70 70%, #8a5560 100%);
  }
  .family-icon {
    position: absolute; left: 168px; top: 2px; width: 91px; height: 126px;
    clip-path: polygon(0 22%, 50% 0, 100% 22%, 100% 100%, 0 100%);
    background: linear-gradient(180deg, #a9803a 0%, #b8222a 45%, #8e1c22 100%);
  }
  .mission {
    position: absolute; left: 150px; right: 150px; top: 236px;
    text-align: center;
    font-family: "Roboto", sans-serif; font-weight: 500;
    font-size: 17px; line-height: 23px;
    color: var(--white);
    text-shadow: 0 1px 3px rgba(0,0,0,0.45);
  }
  .title {
    position: absolute; left: 0; right: 0; top: 300px;
    text-align: center;
    font-family: "Outfit", sans-serif; font-weight: 700;
    font-size: 74px; line-height: 1; letter-spacing: -1px;
    color: var(--white);
  }
  .meeting-band {
    position: absolute; left: 0; top: 391px; width: 977px; height: 59px;
    background: var(--gold-band);
    display: flex; align-items: center; justify-content: center;
    font-family: "Roboto", sans-serif; font-weight: 700;
    font-size: 44px; color: var(--ink-dark);
  }
  .locations {
    position: absolute; left: 0; top: 450px; width: 977px; height: 248px;
  }
  .location {
    position: absolute; width: 420px; margin-left: -210px;
    text-align: center; white-space: nowrap;
    font-family: "Roboto", sans-serif; font-weight: 700;
    color: var(--yellow);
  }
  .location .place { font-size: 27px; line-height: 42px; }
  .location .time { font-size: 30px; line-height: 46px; letter-spacing: 0.5px; }
  .col-left { left: 263px; }
  .col-right { left: 707px; }
  .row-top { top: 24px; }
  .row-bottom { top: 131px; }
  .rule {
    position: absolute; top: 125px; height: 2px; background: var(--white);
  }
  .rule-left { left: 90px; width: 362px; }
  .rule-right { left: 526px; width: 362px; }
  .column-divider {
    position: absolute; left: 477px; top: 36px; width: 1px; height: 174px;
    background: var(--white);
  }
</style>
</head>
<body>
  <main class="postcard">
    <section class="hero">
      <div class="group-photo" role="img" aria-label="Foto grupal de familias de la comunidad al aire libre en un parque, con árboles verdes de fondo"></div>
      <div class="family-icon" role="img" aria-label="Ícono de la Sagrada Familia en marco dorado"></div>
      <p class="mission">Familias que se forman en la fe y valores humanos, y trabajan para llevar a otras familias al encuentro con Cristo y la Virgen María.</p>
      <h1 class="title">Casas de Nueva Aurora</h1>
    </section>

    <div class="meeting-band">Reuniones Cada Domingo</div>

    <section class="locations">
      <div class="location col-left row-top">
        <div class="place">Monte Tabor Alto, Falls Church:</div>
        <div class="time">11:15am - 301-555-0142</div>
      </div>
      <div class="location col-right row-top">
        <div class="place">Luz Divina Norte, Sterling:</div>
        <div class="time">9:30am - 571-555-0187</div>
      </div>
      <div class="rule rule-left"></div>
      <div class="rule rule-right"></div>
      <div class="column-divider"></div>
      <div class="location col-left row-bottom">
        <div class="place">Hogar Manassas Park,</div>
        <div class="time">9:45am - 703-555-0129</div>
      </div>
      <div class="location col-right row-bottom">
        <div class="place">Paz Eterna Sur, Winchester:</div>
        <div class="time">2:30pm - 540-555-0163</div>
      </div>
    </section>
  </main>
</body>
</html>
```